Simple, Professional and neat business card design for Vendralo Inc.

We're looking to re-vamp our business card design. We're a supplier of innovative feed ingredients for the North American animal agriculture industry. We are located in Lucknow, Ontario, Canada and our flagship product is a product that prevents milk fever in dairy cows when the calve, it is fed before calving and is very effective compared to other alternatives available on the market today.

Our company has Danish roots and we import all of our product from our Danish partner/manufacturer in Denmark. We like our design to embrace high professionalism while remaining neat and simple.

Target Market(s)

B2B, Feed Mills, Veterinary Clinics, Large integrators/producers,

Industry/Entity Type

Agribusiness

Contact Information for Business Card

We like the rounded corners because they make the card easy to sit in a wallet and not many use it so it makes the card stand out, just possibly something to take account for during the design.

As you can also see on the sliders below, looking for a that simple but proffesional scandinavian design.

Requirements
Nice to have
• Rounded corners
Should not have
• Too vibrant

```html
<!DOCTYPE html>
<html lang="en">
<head>
<meta charset="utf-8">
<title>Vendralo Inc. – Business Card</title>
<link href="https://fonts.googleapis.com/css2?family=Montserrat:wght@400;500;700;800&display=swap" rel="stylesheet">
<style>
  :root {
    --brand-blue: #0f5fb0;
    --brand-navy: #26333f;
    --card-dark: #1c1c1d;
    --card-light: #ffffff;
    --ink: #2a2a2a;
    --page-bg: #e6e7e9;
  }
  * { box-sizing: border-box; margin: 0; padding: 0; }
  html, body {
    width: 1200px; height: 900px; overflow: hidden;
    background: var(--page-bg);
    font-family: "Montserrat", sans-serif;
  }
  .stage {
    position: relative; width: 1200px; height: 900px;
    display: flex; flex-direction: column; align-items: center; justify-content: center; gap: 44px;
  }
  .card {
    position: relative; width: 630px; height: 360px;
    border-radius: 20px; overflow: hidden;
    box-shadow: 0 10px 28px rgba(0,0,0,.18);
  }
  /* Back */
  .card--back { background: var(--card-dark); display: flex; align-items: center; justify-content: center; }
  .brand { display: flex; align-items: center; gap: 16px; }
  .brand__dot { width: 48px; height: 48px; border-radius: 50%; background: var(--brand-blue); }
  .brand__name { color: var(--brand-blue); font-weight: 800; font-size: 40px; letter-spacing: .5px; }

  /* Front */
  .card--front { background: var(--card-light); }
  .front__wave { position: absolute; inset: 0; }
  .front__logo {
    position: absolute; left: 36px; top: 62px; width: 290px;
    display: flex; flex-direction: column; align-items: center; gap: 12px;
  }
  .front__logo .brand__dot { width: 56px; height: 56px; }
  .front__logo .brand__name { font-size: 35px; }
  .front__divider {
    position: absolute; left: 350px; top: 52px; width: 2px; height: 190px;
    background: var(--brand-blue);
  }
  .contact { position: absolute; left: 374px; top: 52px; color: var(--ink); }
  .contact__name { color: var(--brand-blue); font-weight: 800; font-size: 23px; line-height: 1.1; }
  .contact__role { font-size: 15px; font-weight: 500; margin-bottom: 10px; }
  .contact__list { list-style: none; font-size: 15px; line-height: 23px; }
  .contact__list li { display: flex; align-items: center; gap: 9px; }
  .contact__list svg { width: 12px; height: 12px; fill: var(--brand-blue); flex: none; }
  .contact__address { margin-top: 6px; font-size: 15px; line-height: 21px; }
  .tollfree {
    position: absolute; left: 28px; top: 262px;
    color: #fff; font-size: 14px; font-weight: 500;
    transform: rotate(11deg); transform-origin: left top;
  }
</style>
</head>
<body>
<main class="stage">
  <section class="card card--back" aria-label="Card back">
    <div class="brand">
      <span class="brand__dot"></span>
      <span class="brand__name">VENDRALO INC.</span>
    </div>
  </section>

  <section class="card card--front" aria-label="Card front">
    <svg class="front__wave" viewBox="0 0 630 360" preserveAspectRatio="none" aria-hidden="true">
      <path d="M0,236 C130,248 240,318 630,320 L630,334 C230,332 120,262 0,250 Z" fill="var(--brand-navy)"/>
      <path d="M0,250 C120,262 230,332 630,334 L630,360 L0,360 Z" fill="var(--brand-blue)"/>
    </svg>

    <div class="front__logo">
      <span class="brand__dot"></span>
      <span class="brand__name">VENDRALO INC.</span>
    </div>

    <div class="front__divider"></div>

    <div class="contact">
      <p class="contact__name">Anders Holmgaard</p>
      <p class="contact__role">Founder</p>
      <ul class="contact__list">
        <li><svg viewBox="0 0 12 12"><path d="M2.5 1l2 2.2-1 1.3c.6 1.5 1.6 2.5 3 3.1l1.3-1L10 8.5 9 10.8C5 10.5 1.5 7 1.2 2.6z"/></svg>519-204-6180</li>
        <li><svg viewBox="0 0 12 12"><path d="M3 0h6v12H3zM4 1.5v8h4v-8z"/></svg>519-204-7731</li>
        <li><svg viewBox="0 0 12 12"><path d="M2 4h8v6H2zM3.5 0h5v3.5h-5z"/></svg>519-204-7742</li>
        <li><svg viewBox="0 0 12 12"><path d="M0 2h12v8H0zM1.2 3l4.8 3.6L10.8 3z" fill-rule="evenodd"/></svg>anders@vendralo.com</li>
        <li><svg viewBox="0 0 12 12"><circle cx="6" cy="6" r="5.5"/></svg>www.vendralo.com</li>
      </ul>
      <p class="contact__address">Box 412, Fernbrook,<br>Ontario Canada N0H 3K0</p>
    </div>

    <p class="tollfree">Toll Free: 888-470-2916</p>
  </section>
</main>
</body>
</html>
```